Bref créative
Business card and stationery for painting company
Brightcoat finishes
Professional
Marek Dolvan
Owner
318 S Harlow Ave suite 204
Villa Park, IL 60139
marek.dolvan@brightcoatfinishes.com
www.brightcoatfinishes.com
this is file of my logo
vector logo file

```html
<!DOCTYPE html>
<html lang="en">
<head>
<meta charset="utf-8">
<title>Brightcoat finishes – Stationery</title>
<link href="https://fonts.googleapis.com/css2?family=Open+Sans:wght@400;700&display=swap" rel="stylesheet">
<style>
:root{
  --stage-light:#6e6e6e;
  --stage-dark:#3e3e3e;
  --paper:#ffffff;
  --paper-shade:#eeeeee;
  --brand-red:#c8202b;
  --brand-blue:#1c4f9e;
  --ink:#444444;
  --ink-soft:#8a8a8a;
  --label:#cfcfcf;
}
*{box-sizing:border-box;margin:0;padding:0}
html,body{width:1200px;height:437px;overflow:hidden}
body{
  font-family:"Open Sans",Arial,sans-serif;
  background:radial-gradient(ellipse at 50% 45%,var(--stage-light),var(--stage-dark));
  position:relative;
}
.piece{position:absolute;box-shadow:0 3px 8px rgba(0,0,0,.45)}
.label{position:absolute;font-size:7px;color:var(--label);text-align:center;width:140px}

.brand{display:flex;align-items:center;gap:4px;color:var(--brand-red);font-weight:700;white-space:nowrap}
.brand-dot{width:8px;height:8px;border-radius:50%;background:var(--brand-blue)}

/* business card */
.card{width:134px;height:77px;border-radius:5px;background:var(--paper)}
.card-front{left:34px;top:180px;padding:9px 8px}
.card-front .brand{font-size:6px}
.card-front .brand-dot{width:5px;height:5px}
.card-name{font-size:5px;font-weight:700;color:var(--ink);margin-top:6px}
.card-role{font-size:4px;color:var(--ink-soft)}
.card-lines{font-size:3.6px;color:var(--ink);line-height:1.5;margin-top:5px}
.card-front .strip{position:absolute;left:0;right:0;bottom:0;height:6px;background:var(--brand-red);border-radius:0 0 5px 5px}
.card-back{left:34px;top:312px;background:var(--brand-red);display:flex;flex-direction:column;align-items:center;justify-content:center;gap:6px}
.card-back .brand{color:var(--paper);font-size:7px}
.card-back .brand-dot{background:var(--paper)}
.card-back .web{font-size:4px;color:var(--paper)}

/* letterhead */
.letterhead{width:288px;height:389px;top:19px;background:var(--paper)}
.lh-1{left:211px}
.lh-2{left:523px}
.letterhead .head{position:absolute;top:14px}
.lh-1 .head{left:18px;font-size:9px}
.lh-2 .head{left:50%;transform:translateX(-50%);font-size:9px}
.lh-1 .contact{position:absolute;left:110px;top:12px;font-size:4px;line-height:1.6;color:var(--ink)}
.watermark{position:absolute;left:74px;top:120px;width:140px;height:100px;border-radius:50%;background:radial-gradient(circle,rgba(200,32,43,.08),rgba(28,79,158,.03) 70%,transparent)}
.footer{position:absolute;left:0;right:0;bottom:0}
.footer .web{font-size:4px;color:var(--ink);text-align:center;padding-bottom:4px}
.footer .band{height:8px;background:var(--brand-red);border-top:2px solid var(--brand-blue)}

/* envelopes */
.envelope{left:835px;width:341px;background:var(--paper-shade)}
.env-1{top:19px;height:106px}
.env-2{top:132px;height:101px}
.env-3{top:252px;height:84px;background:var(--paper)}
.env-4{top:336px;height:77px;background:var(--paper);padding:8px 10px}
.envelope svg{position:absolute;left:0;top:0;width:100%;height:100%}
.env-2 .brand,.env-1 .brand{position:absolute;left:50%;transform:translateX(-50%);font-size:6px}
.env-1 .brand{top:24px}
.env-2 .brand{top:30px;color:var(--paper)}
.env-2 .brand-dot{background:var(--paper)}
.env-3 .brand{position:absolute;left:12px;top:40px;font-size:5px}
.env-4 .brand{font-size:8px}
.env-4 .addr{font-size:4px;line-height:1.6;color:var(--ink);margin-top:3px}
</style>
</head>
<body>

<section class="piece card card-front">
  <div class="brand"><span class="brand-dot"></span>Brightcoat finishes</div>
  <p class="card-name">Marek Dolvan</p>
  <p class="card-role">Owner</p>
  <div class="card-lines">
    <p>318 S Harlow Ave suite 204</p>
    <p>Villa Park, IL 60139</p>
    <p>marek.dolvan@brightcoatfinishes.com</p>
    <p>www.brightcoatfinishes.com</p>
  </div>
  <span class="strip"></span>
</section>
<p class="label" style="left:31px;top:262px">Front Side</p>

<section class="piece card card-back">
  <div class="brand"><span class="brand-dot"></span>Brightcoat finishes</div>
  <p class="web">www.brightcoatfinishes.com</p>
</section>
<p class="label" style="left:31px;top:394px">Back Side</p>

<section class="piece letterhead lh-1">
  <div class="brand head"><span class="brand-dot"></span>Brightcoat finishes</div>
  <div class="contact">
    <p>318 S Harlow Ave suite 204</p>
    <p>Villa Park, IL 60139</p>
    <p>marek.dolvan@brightcoatfinishes.com</p>
  </div>
  <div class="watermark" role="img" aria-label="Faint brand mark area"></div>
  <div class="footer"><p class="web">www.brightcoatfinishes.com</p><div class="band"></div></div>
</section>
<p class="label" style="left:285px;top:414px">Letterhead option 1</p>

<section class="piece letterhead lh-2">
  <div class="brand head"><span class="brand-dot"></span>Brightcoat finishes</div>
  <div class="watermark" role="img" aria-label="Faint brand mark area"></div>
  <div class="footer"><p class="web">318 S Harlow Ave suite 204 · Villa Park, IL 60139 · www.brightcoatfinishes.com</p><div class="band"></div></div>
</section>
<p class="label" style="left:597px;top:414px">Letterhead option 2</p>

<section class="piece envelope env-1">
  <svg viewBox="0 0 341 106" preserveAspectRatio="none"><path d="M0 0H341L170.5 62Z" fill="#ffffff"/><path d="M0 0L170.5 62L341 0" fill="none" stroke="var(--brand-red)" stroke-width="3"/></svg>
  <div class="brand"><span class="brand-dot"></span>Brightcoat finishes</div>
</section>
<section class="piece envelope env-2">
  <svg viewBox="0 0 341 101" preserveAspectRatio="none"><path d="M0 0H341L170.5 62Z" fill="var(--brand-blue)"/></svg>
  <div class="brand"><span class="brand-dot"></span>Brightcoat finishes</div>
</section>
<section class="piece envelope env-3">
  <svg viewBox="0 0 341 84" preserveAspectRatio="none"><path d="M0 0L170.5 40L341 0" fill="none" stroke="#dddddd" stroke-width="1"/></svg>
  <div class="brand"><span class="brand-dot"></span>Brightcoat finishes</div>
</section>
<section class="piece envelope env-4">
  <div class="brand"><span class="brand-dot"></span>Brightcoat finishes</div>
  <div class="addr">
    <p>318 S Harlow Ave suite 204</p>
    <p>Villa Park, IL 60139</p>
  </div>
</section>
<p class="label" style="left:935px;top:418px">Envelope Front &amp; Back</p>

</body>
</html>
```